3 Politically Incorrect Greeting Cards

I would like to see some clean, colorful, and modern designs for 3 "politically incorrect" greeting cards aimed at young, single, successful women. I would like them to say:

Card 1: " Congratulations on not marrying the wrong person"
Card 2: " Congratulations on buying a house without a husband"
Card 3: " Thank you for not forgetting about me now that you have a boyfriend"

My initial thought was to have a white background with simple black writing, but I think a colorful background with a white text box in the middle might be more appropriate. I can't imagine the cards having any images/icons on them, but I'm open to suggestions if you think it would improve on the design. You guys are likely more creative than I am.

I've included a couple pics of looks I like - but like I said - I'm open to suggestions and what I like may not be appropriate for these cards. All the cards can have a similar esthetic or theme (maybe the same fonts but different colors or different color florals in each) or they can be completely different.

Target Market(s)

Young, single, successful women mid-20s to mid 40's.

Font styles to use
Serif
Sans Serif
Other font styles liked:
• Watercolour lettering maybe

Colors

Designer to choose colors to be used in the design.

Requirements
Must have
• Clean, colorful, bright, professional looking. The right tone for the message.
• I think the message is bold so the writing and colors have to be as well. I have included examples of ideas I like.
Nice to have
• Images, illustrations, icons, maybe patterns or some decorative details. Something to make the card more interesting than just the words (like the blue background with black letters one I made). I like a bright pattern with a white box in the center with the text.
Should not have
• Special effects, galaxy pictures, ugly images, bland colors.

```html
<!DOCTYPE html>
<html lang="en">
<head>
<meta charset="utf-8">
<title>Congratulations Card</title>
<link rel="stylesheet" href="https://fonts.googleapis.com/css2?family=Fondamento:ital@1&display=swap">
<style>
  :root {
    --teal-deep: #1aaea6;
    --teal-mid: #4fc4bb;
    --teal-soft: #8fd8cf;
    --teal-pale: #c4ece6;
    --plaque-edge: #9fe0d9;
    --motif-tone: #5cc9c1;
    --ink-white: #ffffff;
    --page: #ffffff;
  }
  html, body {
    margin: 0;
    padding: 0;
    width: 1200px;
    height: 965px;
    overflow: hidden;
    background: var(--page);
  }
  .card {
    position: relative;
    width: 1200px;
    height: 965px;
    overflow: hidden;
  }
  .card__pattern {
    position: absolute;
    inset: 0;
    background:
      radial-gradient(ellipse at 20% 25%, var(--teal-pale) 0%, transparent 45%),
      radial-gradient(ellipse at 80% 80%, var(--teal-pale) 0%, transparent 40%),
      linear-gradient(135deg, var(--teal-soft) 0%, var(--teal-mid) 50%, var(--teal-soft) 100%);
  }
  .card__plaque {
    position: absolute;
    left: 206px;
    top: 276px;
    width: 777px;
    height: 387px;
    box-sizing: border-box;
    background: var(--teal-deep);
    border: 4px solid var(--plaque-edge);
    border-radius: 60px;
  }
  .card__motif {
    position: absolute;
    left: 50%;
    top: 53px;
    width: 90px;
    height: 34px;
    margin-left: -45px;
    border-radius: 17px;
    background: var(--motif-tone);
  }
  .card__message {
    position: absolute;
    left: 0;
    right: 0;
    top: 115px;
    margin: 0;
    text-align: center;
    font-family: "Fondamento", cursive;
    font-style: italic;
    font-weight: 400;
    font-size: 40px;
    line-height: 74px;
    color: var(--ink-white);
  }
</style>
</head>
<body>
  <main class="card">
    <div class="card__pattern" role="img" aria-label="Teal watercolour lattice pattern background"></div>

    <section class="card__plaque">
      <div class="card__motif" role="img" aria-label="Small heart with arrow ornament"></div>
      <p class="card__message">Congratulations<br>on not marrying the<br>wrong person</p>
    </section>
  </main>
</body>
</html>
```